New book cover for existing E-Bike tour book

I would like to update the current design of my book "Pedelec Rides through the Hazelmark" (translation: Pedelec Rides through the Hazelmark) and make it more modern.

Existing Book:
Title: "Pedelec rides through the Hazelmark"
Subtitle: 40 eventful tours with nature and culture.
Info bar with three elements:
 Unique sights
 Cozy beer gardens
 The most beautiful bike paths

objectives:
- to make the design more modern
- to make it attractive for people who want to ride E-bike

Requirements for the new design:

1. All texts for title, subtitle and info bar should be kept.
Font, color and placement can be changed.

2. the 5 nature images below the title are optional: can be used, can be replaced, can be omitted

3. the background image is optional: can be used or can be replaced with a totally different background.

Target Market(s)

People who want to discover the "Odenwald" region with the E-Bike

Font styles to use
Sans Serif

Requirements
Must have
• all texts for title, subtitle and info bar should be kept.
Nice to have
• It would be nice to see two E-bike riders. Like on the original book cover but just bigger in size. The two E-Bike riders on the original cover are a bit small.

```html
<!DOCTYPE html>
<html lang="en">
<head>
<meta charset="utf-8">
<title>Pedelec Rides through the Hazelmark – Book Cover</title>
<link rel="stylesheet" href="https://fonts.googleapis.com/css2?family=Arimo:wght@400;700&family=Permanent+Marker&family=Roboto+Condensed:wght@700&display=swap">
<style>
  :root {
    --stage: #5e5e5e;
    --sky-deep: #1c5cc2;
    --sky: #3f87d9;
    --haze: #9fb3c2;
    --rock: #7a6d52;
    --forest: #2e4727;
    --meadow: #7f8b3e;
    --gravel: #aaa69d;
    --yellow: #f7ef00;
    --white: #ffffff;
    --ink: #111111;
  }
  * { box-sizing: border-box; margin: 0; padding: 0; }
  html, body { width: 1200px; height: 840px; overflow: hidden; background: var(--stage); }
  .cover {
    position: absolute; left: 33px; top: 35px; width: 1133px; height: 773px;
    box-shadow: 4px 6px 10px rgba(0,0,0,.45);
    overflow: hidden;
  }
  .cover__scene {
    position: absolute; inset: 0;
    background: linear-gradient(180deg,
      var(--sky-deep) 0%, var(--sky) 30%, var(--haze) 43%,
      var(--rock) 52%, var(--forest) 68%, var(--forest) 78%,
      var(--meadow) 88%, var(--gravel) 100%);
  }
  .brush { font-family: "Permanent Marker", "Arimo", sans-serif; color: var(--yellow); }
  .condensed { font-family: "Roboto Condensed", "Arimo", sans-serif; font-weight: 700; color: var(--white); }

  /* back */
  .back__title {
    position: absolute; left: 0; width: 546px; top: 42px; text-align: center;
    font-size: 31px; line-height: 1.2; white-space: nowrap;
  }
  .back__title .brush { font-size: 30px; }
  .back__blurb {
    position: absolute; left: 52px; width: 437px;
    font-family: "Arimo", sans-serif; font-size: 13.2px; line-height: 18px;
    color: var(--white); text-align: justify;
  }
  .back__blurb--one { top: 101px; }
  .back__blurb--two { top: 317px; }
  .back__gallery {
    position: absolute; left: 52px; top: 548px; width: 437px; height: 93px;
    border: 2px solid var(--white); background: var(--white);
    display: flex; flex-direction: column;
  }
  .gallery__photos { display: flex; gap: 2px; height: 63px; }
  .gallery__photo { flex: 1; }
  .gallery__photo--village { background: linear-gradient(180deg, #b9c9d6, #6d8a4c 55%, #8a7a4c); }
  .gallery__photo--lake { background: linear-gradient(180deg, #6aa3d8, #4c7b3a 55%, #7fa3b4); }
  .gallery__photo--autumn { background: linear-gradient(180deg, #6f8f4a, #d9b92a 50%, #5f8a3c); }
  .gallery__photo--hills { background: linear-gradient(180deg, #3a72c0, #5b7a36 50%, #a9b748); }
  .gallery__photo--road { background: linear-gradient(180deg, #86b2e0, #3f6a2e 55%, #8f9a88); }
  .gallery__caption {
    flex: 1; margin-top: 2px; background: var(--yellow); color: var(--ink);
    font-family: "Arimo", sans-serif; font-size: 13.5px;
    display: flex; align-items: center; justify-content: center;
  }

  /* spine */
  .spine {
    position: absolute; left: 546px; width: 42px; top: 0; height: 773px;
  }
  .spine__title, .spine__author {
    position: absolute; left: 0; width: 42px;
    writing-mode: vertical-rl; display: flex; align-items: center;
    white-space: nowrap;
  }
  .spine__title { top: 33px; font-size: 24px; }
  .spine__title .brush { font-size: 22px; margin-bottom: 4px; }
  .spine__author {
    top: 544px; font-family: "Arimo", sans-serif; font-weight: 700;
    font-size: 23px; color: var(--white); letter-spacing: .5px;
  }

  /* front */
  .front__tagline {
    position: absolute; left: 630px; width: 470px; top: 28px; text-align: center;
    font-family: "Arimo", sans-serif; font-weight: 700; font-size: 18.5px;
    color: var(--white); white-space: nowrap;
  }
  .front__kicker {
    position: absolute; left: 630px; width: 470px; top: 62px; text-align: center;
    font-size: 62px; line-height: 1; transform: rotate(-3deg);
  }
  .front__headline {
    position: absolute; left: 620px; width: 490px; top: 128px; text-align: center;
    font-size: 150px; line-height: 1; letter-spacing: -4px; transform: rotate(-3deg);
  }
  .front__place {
    position: absolute; right: 70px; top: 292px; text-align: right;
    font-size: 44px; line-height: 1; white-space: nowrap;
  }
  .front__features {
    position: absolute; left: 700px; width: 330px; top: 486px; list-style: none;
    text-align: center; font-size: 13.5px; line-height: 30px;
    transform: skewX(-6deg);
  }
  .front__author {
    position: absolute; left: 640px; width: 440px; top: 716px; text-align: center;
    font-family: "Arimo", sans-serif; font-weight: 700; font-size: 27px;
    color: var(--white); letter-spacing: .5px;
  }
</style>
</head>
<body>
<div class="cover">
  <div class="cover__scene" role="img" aria-label="Mountain landscape photograph with blue sky, rocky peaks, pine forest and a gravel path where three e-bike riders approach"></div>

  <section class="back">
    <h2 class="back__title"><span class="brush">PEDELEC RIDES</span> <span class="condensed">through the Hazelmark</span></h2>
    <p class="back__blurb back__blurb--one">Lorem ipsum dolor sit amet, consectetur adipiscing elit, sed do eiusmod tempor incididunt ut labore et dolore magna aliqua. Quis ipsum suspendisse ultrices gravida. Risus commodo viverra maecenas accumsan lacus vel facilisis. Lorem ipsum dolor sit amet, consectetur adipiscing elit, sed do eiusmod tempor incididunt ut labore et dolore magna aliqua. Quis ipsum suspendisse ultrices gravida. Risus commodo viverra maecenas accumsan lacus vel facilisis. Lorem ipsum dolor sit amet, consectetur adipiscing elit, sed do eiusmod tempor incididunt ut labore et dolore magna aliqua. Quis ipsum suspendisse ultrices gravida. Risus commodo viverra maecenas accumsan lacus vel facilisis.</p>
    <p class="back__blurb back__blurb--two">Lorem ipsum dolor sit amet, consectetur adipiscing elit, sed do eiusmod tempor incididunt ut labore et dolore magna aliqua. Quis ipsum suspendisse ultrices gravida. Risus commodo viverra maecenas accumsan lacus vel facilisis. Lorem ipsum dolor sit amet, consectetur adipiscing elit, sed do eiusmod tempor incididunt ut labore et dolore magna aliqua. Quis ipsum suspendisse ultrices gravida. Risus commodo viverra maecenas accumsan lacus vel facilisis. Lorem ipsum dolor sit amet, consectetur adipiscing elit, sed do eiusmod tempor incididunt ut labore et dolore magna aliqua. Quis ipsum suspendisse ultrices gravida. Risus commodo viverra maecenas accumsan lacus vel facilisis.</p>
    <div class="back__gallery">
      <div class="gallery__photos">
        <div class="gallery__photo gallery__photo--village" role="img" aria-label="Village among autumn fields beside a country road"></div>
        <div class="gallery__photo gallery__photo--lake" role="img" aria-label="Forested hill above a lake"></div>
        <div class="gallery__photo gallery__photo--autumn" role="img" aria-label="Yellow autumn tree beside a footpath"></div>
        <div class="gallery__photo gallery__photo--hills" role="img" aria-label="Green rolling hills under a blue sky"></div>
        <div class="gallery__photo gallery__photo--road" role="img" aria-label="Winding road through green countryside"></div>
      </div>
      <div class="gallery__caption">40 eventful tours with nature and culture</div>
    </div>
  </section>

  <section class="spine">
    <div class="spine__title"><span class="brush">PEDELEC RIDES</span>&nbsp;<span class="condensed">through the Hazelmark</span></div>
    <div class="spine__author">KONRAD WIESLER</div>
  </section>

  <section class="front">
    <p class="front__tagline">40 EVENTFUL TOURS WITH NATURE AND CULTURE</p>
    <h1>
      <span class="front__kicker brush">PEDELEC</span>
      <span class="front__headline brush">RIDES</span>
      <span class="front__place condensed">through the Hazelmark</span>
    </h1>
    <ul class="front__features brush">
      <li>UNIQUE SIGHTS</li>
      <li>COZY BEER GARDENS</li>
      <li>THE MOST BEAUTIFUL BIKE PATHS</li>
    </ul>
    <p class="front__author">KONRAD WIESLER</p>
  </section>
</div>
</body>
</html>
```